Travel agency website refresh

I want to refresh and simplify my current Wordpress.com website. Same general color scheme but modernize and make it user friendly for all devices. Must work with Wordpress. No live booking engines. We are a boutique luxury travel agency. Think luxury, vacation, boho chic, elegant, lush, tropical, cruises, first class. Romance and adventure.
Updates

I’ve guaranteed the project so I’m hoping to see more quality entries to make a decision

Target Market(s)

Luxury travelers

Industry/Entity Type

Travel

Coding

Coded - Design and coding required

Number of Pages Required

5+ page

Font styles to use
Sans Serif

Colors
0094D4
00A9DD
6FCCEA
C7EBF8
E9F6FB

Requirements
Must have
• Compatible with Wordpress.com, homepage, about page, contact page, faq page
Nice to have
• The homepage should quickly tell the consumer the type of travel I specialize in. My current website has this (journeywithmerel.example). I’d like to incorporate the about me as a preview on the home page.
Should not have
• Harsh colors, look generic

```html
<!DOCTYPE html>
<html lang="en">
<head>
<meta charset="utf-8">
<title>Travel by Merel — Boutique Travel Agency</title>
<link href="https://fonts.googleapis.com/css2?family=Jost:wght@400;500;600&family=Playfair+Display:wght@400;700;800&family=Poppins:wght@400;500&display=swap" rel="stylesheet">
<style>
:root{
  --teal:#68c9c3;
  --teal-dark:#4fb8b1;
  --teal-light:#c9eeec;
  --ink:#1c1c1c;
  --text:#555;
  --muted:#8a8a8a;
  --taupe:#c0a89b;
  --panel:#f7f7f7;
  --white:#fff;
}
*{box-sizing:border-box;margin:0;padding:0}
html,body{width:1200px;height:4478px;overflow:hidden}
body{position:relative;background:var(--white);font-family:"Jost",sans-serif;color:var(--text)}
.abs{position:absolute}
.photo{position:absolute}
.btn{position:absolute;background:var(--teal);color:#fff;font-family:"Jost",sans-serif;font-size:17px;border-radius:5px;display:flex;align-items:center;justify-content:center}

/* header */
.brand{position:absolute;left:102px;top:14px;width:170px;text-align:center}
.brand-mark{width:62px;height:62px;border-radius:50%;background:var(--teal-light);margin:0 auto 4px}
.brand-name{font-family:"Jost",sans-serif;font-weight:600;font-size:19px;color:#6b6b6b;letter-spacing:.5px;white-space:nowrap}
.nav{position:absolute;top:33px;left:444px;display:flex;gap:26px;font-size:21px;font-weight:500;color:var(--ink)}
.nav a{color:inherit;text-decoration:none;padding-bottom:4px}
.nav .active{border-bottom:3px solid var(--teal)}
.header-phone{position:absolute;left:944px;top:33px;font-size:21px;font-weight:500;color:var(--ink);display:flex;align-items:center;gap:8px}

/* hero */
.hero-title{position:absolute;top:162px;width:100%;text-align:center;font-family:"Playfair Display",serif;color:var(--ink)}
.hero-title .small{font-size:36px;font-weight:400}
.hero-title .big{font-size:46px;font-weight:800;letter-spacing:1px}
.hero-lead{position:absolute;top:228px;width:100%;text-align:center;font-size:18px;line-height:27px;color:#555}

/* services */
.service-title{position:absolute;text-align:center;color:var(--teal);font-size:20px;letter-spacing:.5px}
.service-text{position:absolute;text-align:center;font-size:11.5px;line-height:17px;color:#555}
.arrow{position:absolute;font-size:30px;color:#333;font-weight:300}

/* about */
.about-box{position:absolute;left:237px;top:1355px;width:440px;height:440px;background:#fff}
.section-h{font-family:"Jost",sans-serif;color:var(--teal);font-weight:500}
.about-text{font-size:18px;line-height:29px;color:#555}

/* testimonials */
.t-card{position:absolute;top:2085px;width:333px;height:326px;background:#fff;border-radius:14px;box-shadow:0 2px 10px rgba(0,0,0,.06);border-bottom:4px solid var(--teal)}
.t-card::before{content:"";position:absolute;left:0;top:150px;bottom:-4px;width:4px;background:var(--teal);border-radius:0 0 0 14px}
.t-card::after{content:"";position:absolute;right:0;top:150px;bottom:-4px;width:4px;background:var(--teal);border-radius:0 0 14px 0}
.avatar{position:absolute;left:96px;top:18px;width:136px;height:136px;border-radius:50%;border:5px solid var(--teal)}
.quote-mark{position:absolute;left:14px;top:150px;font-family:"Playfair Display",serif;font-size:54px;color:#ddd;line-height:1}
.t-text{position:absolute;left:20px;right:18px;top:188px;font-size:16px;line-height:26px;color:#444}
.t-name{position:absolute;top:262px;font-size:15px;line-height:25px;color:#444}

/* contact */
.form-box{position:absolute;left:700px;top:2498px;width:413px;height:397px;background:var(--teal)}
.form-box h3{position:absolute;left:20px;top:22px;font-size:31px;font-weight:500;color:#fff}
.form-box p{position:absolute;left:22px;top:64px;font-size:12px;color:#eefaf9}
.field{position:absolute;background:#e6f6f5;font-size:10px;color:#888;padding:8px 10px}
.send{position:absolute;left:22px;top:340px;width:368px;height:32px;background:#fff;font-size:11px;font-weight:600;color:#222;display:flex;align-items:center;justify-content:center}

/* faq */
.faq-h1{position:absolute;top:3362px;width:100%;text-align:center;font-size:28px;letter-spacing:15px;color:var(--teal);font-weight:500}
.faq-h2{position:absolute;top:3404px;width:100%;text-align:center;font-size:40px;letter-spacing:20px;color:var(--taupe);font-weight:500}
.faq{position:absolute;width:500px;height:54px;background:var(--panel);font-family:"Poppins",sans-serif;font-size:15px;color:#222;padding:0 48px 0 12px;display:flex;align-items:center;line-height:18px}
.faq::after{content:"+";position:absolute;right:18px;top:50%;transform:translateY(-50%);font-size:24px;color:#222;font-weight:400}
.faq.open{height:192px;align-items:flex-start;flex-direction:column;padding-top:18px;border:1px solid #eee;background:#fff}
.faq.open::after{content:"—";top:30px;font-size:18px}
.faq.open .ans{margin-top:30px;font-size:14px;line-height:20px;color:#777;padding-right:40px}

/* footer */
.foot-h{position:absolute;top:4312px;font-size:15px;color:var(--teal)}
.foot-list{position:absolute;top:4338px;font-size:15px;line-height:29px;color:#444;list-style:none}
.foot-list li::before{content:"›";color:var(--teal);margin-right:6px}
.bottom-bar{position:absolute;left:0;top:4440px;width:1200px;height:38px;background:var(--teal);color:#fff;font-size:12px;display:flex;align-items:center;justify-content:center;letter-spacing:.3px}
</style>
</head>
<body>

<header>
  <div class="brand"><div class="brand-mark"></div><div class="brand-name">TRAVEL by MEREL</div></div>
  <nav class="nav"><a href="#">Home</a><a href="#" class="active">About</a><a href="#">Contact</a><a href="#">Faq</a></nav>
  <div class="header-phone">
    <svg width="18" height="18" viewBox="0 0 24 24"><path fill="#68c9c3" d="M6.6 10.8a15.1 15.1 0 0 0 6.6 6.6l2.2-2.2c.3-.3.7-.4 1-.2 1.1.4 2.3.6 3.6.6.6 0 1 .4 1 1V20c0 .6-.4 1-1 1A17 17 0 0 1 3 4c0-.6.4-1 1-1h3.5c.6 0 1 .4 1 1 0 1.3.2 2.5.6 3.6.1.3 0 .7-.2 1z"/></svg>
    555-014-2290
  </div>
</header>

<section class="hero">
  <div class="photo" role="img" aria-label="Coastal highland landscape with rock pinnacle, green hills and sea loch" style="left:0;top:250px;width:1200px;height:520px;background:linear-gradient(180deg,#fff 0%,#cfdbe2 12%,#8aa7b8 30%,#6f8f5a 52%,#a8b83a 68%,#c9cf58 78%,#fff 100%)"></div>
  <h1 class="hero-title"><span class="small">Welcome to </span><span class="big">TRAVEL BY MEREL</span></h1>
  <p class="hero-lead">Travel by Merel is a boutique travel agency headquartered in Alder Falls, Vermont<br>owned and operated by Merel Haines.</p>
  <a class="btn" style="left:533px;top:300px;width:133px;height:34px">Read More</a>
</section>

<section class="services">
  <span class="arrow" style="left:85px;top:955px">‹</span>
  <span class="arrow" style="left:1097px;top:955px">›</span>
  <div class="photo" role="img" aria-label="Cruise ship in a mountain fjord" style="left:137px;top:842px;width:300px;height:238px;background:linear-gradient(180deg,#c7d3dc,#6f8a6c 45%,#2f7090 75%,#245f7c)"></div>
  <div class="photo" role="img" aria-label="Traveler with suitcase waiting at an airport" style="left:437px;top:823px;width:326px;height:259px;background:linear-gradient(180deg,#d9d4c8,#b7a895 50%,#8c7a66)"></div>
  <div class="photo" role="img" aria-label="Couple walking on a pier to overwater villas" style="left:762px;top:842px;width:300px;height:238px;background:linear-gradient(180deg,#4e7fb8,#8fb3d0 40%,#7a6a5a 70%,#a39380)"></div>

  <div class="service-title" style="left:137px;top:1096px;width:300px">CRUISING</div>
  <p class="service-text" style="left:147px;top:1132px;width:280px">According to the Ocean Voyage Council, almost 70 percent of travelers book their cruises with a travel agent</p>
  <a class="btn" style="left:226px;top:1209px;width:124px;height:31px;font-size:16px">Read More</a>

  <div class="service-title" style="left:437px;top:1099px;width:326px">CUSTOM TRAVEL</div>
  <p class="service-text" style="left:457px;top:1138px;width:286px">A great trip isn't a one-size-fits-all proposition. Rather, your greatest adventures are uniquely your size, reflecting your style and budget.</p>
  <a class="btn" style="left:533px;top:1221px;width:133px;height:34px">Read More</a>

  <div class="service-title" style="left:762px;top:1096px;width:300px">FAMILY VACATIONS</div>
  <p class="service-text" style="left:772px;top:1132px;width:280px">Your family vacation doesn't have to include only those who live in your house. Invite your parents along. Extend an invitation to your siblings.</p>
  <a class="btn" style="left:849px;top:1209px;width:124px;height:31px;font-size:16px">Read More</a>
</section>

<section class="about">
  <div class="photo" role="img" aria-label="Snowy mountain peaks above a sea of clouds" style="left:0;top:1440px;width:1200px;height:500px;background:linear-gradient(180deg,#fff 0%,#cfe0ee 15%,#6d9cc4 40%,#3d5d80 65%,#e9eef3 85%,#fff 100%)"></div>
  <div class="about-box"></div>
  <div class="photo" role="img" aria-label="Portrait of the agency owner" style="left:675px;top:1373px;width:370px;height:427px;background:linear-gradient(160deg,#3a2b22,#6b4a3a 50%,#2a1f19)"></div>
  <h2 class="section-h abs" style="left:262px;top:1362px;font-size:40px">About Me</h2>
  <p class="about-text abs" style="left:262px;top:1429px;width:355px">Travel by Merel is a boutique travel agency headquartered in Alder Falls, Vermont owned and operated by Merel Haines. Merel is a professional travel agent with over 27 years experience.</p>
  <a class="btn" style="left:262px;top:1592px;width:134px;height:32px">Read More</a>
</section>

<section class="testimonials">
  <h2 class="section-h abs" style="top:1980px;width:1200px;text-align:center;font-size:42px">TESTIMONIALS</h2>
  <span class="arrow" style="left:40px;top:2212px">‹</span>
  <span class="arrow" style="left:1140px;top:2212px">›</span>

  <article class="t-card" style="left:83px">
    <div class="avatar" role="img" aria-label="Client portrait" style="background:linear-gradient(160deg,#6a4a35,#2b4f8f)"></div>
    <span class="quote-mark">“</span>
    <p class="t-text">Marco and I had the most amazing time in Napa Valley! Thank for so much for planning our trip!</p>
    <p class="t-name" style="left:172px">-Lena &amp; Marco<br>North Carolina</p>
  </article>
  <article class="t-card" style="left:433px">
    <div class="avatar" role="img" aria-label="Client portrait" style="background:linear-gradient(160deg,#b55f3a,#e9d8cc)"></div>
    <span class="quote-mark">“</span>
    <p class="t-text">Merel is great! She takes care of my travel arrangements every year. From exotic locations to not so exotic.</p>
    <p class="t-name" style="left:184px">-Jolie Barrett<br>California</p>
  </article>
  <article class="t-card" style="left:783px">
    <div class="avatar" role="img" aria-label="Client portrait" style="background:linear-gradient(160deg,#2a2a2a,#d8c3b5)"></div>
    <span class="quote-mark">“</span>
    <p class="t-text">Thank you again for helping to make this trip so successful. We will definitely pass your info on to our friends.</p>
    <p class="t-name" style="left:204px">-R. Okafor<br>New York</p>
  </article>
</section>

<section class="contact">
  <div class="photo" role="img" aria-label="Stone bridge leading to a castle on a loch" style="left:0;top:2560px;width:1200px;height:700px;background:linear-gradient(180deg,#fff 0%,#e7ecee 15%,#b9c2b8 35%,#7a8a55 55%,#a8b63e 72%,#e6ebd8 88%,#fff 100%)"></div>
  <h2 class="abs" style="left:88px;top:2770px;font-size:38px;font-weight:500;color:rgba(255,255,255,.55)">Contact Us</h2>
  <p class="abs" style="left:94px;top:2838px;font-size:18px;color:rgba(255,255,255,.5)">📞 555-014-2290</p>
  <p class="abs" style="left:94px;top:2874px;font-size:14px;color:rgba(255,255,255,.35)">hello@journeywithmerel.example</p>

  <form class="form-box">
    <h3>Send Us Message</h3>
    <p>Lorem Ipsum is simply dummy text of the printing</p>
    <div class="field" style="left:22px;top:102px;width:173px;height:31px">Name</div>
    <div class="field" style="left:215px;top:102px;width:173px;height:31px">Email</div>
    <div class="field" style="left:22px;top:150px;width:173px;height:31px">Phone no.</div>
    <div class="field" style="left:215px;top:150px;width:173px;height:31px">Subject</div>
    <div class="field" style="left:22px;top:197px;width:368px;height:125px">Message</div>
    <div class="send">Send Message</div>
  </form>
</section>

<section class="faqs">
  <h2 class="faq-h1">FREQUENTLY</h2>
  <h2 class="faq-h2">ASKED QUESTION</h2>

  <div class="faq open" style="left:87px;top:3497px">What is travel by merel?<div class="ans">Lorem ipsum dolor sit amet, consectetur adipiscing elit, sed do eiusmod tempor incididunt ut labore et dolore magna aliqua. Quis ipsum suspendisse ultrices gravida. Risus commodo viverra maecenas accumsan lacus vel facilisis.</div></div>
  <div class="faq" style="left:87px;top:3700px">Doesn't it cost more to book with a travel agent?</div>
  <div class="faq" style="left:87px;top:3766px">I've never worked with a travel agent before.<br>what do i need to know? how are you paid?</div>
  <div class="faq" style="left:87px;top:3832px">I have a ton of frequent flyer miles, hotel points,<br>credit card points etc.can you book my trip?</div>
  <div class="faq" style="left:87px;top:3897px">What is the best way to pick a travel agent?</div>
  <div class="faq" style="left:87px;top:3963px">Do you offer payment plans?</div>
  <div class="faq" style="left:87px;top:4029px">What about covid-19?</div>
  <div class="faq" style="left:87px;top:4096px">Should i just book direct with the resort or cruise line?</div>

  <div class="faq" style="left:612px;top:3498px">Where is your office located?</div>
  <div class="faq" style="left:612px;top:3564px">Do you charge service fees?</div>
  <div class="faq" style="left:612px;top:3630px">Is there anything you don't book?</div>
  <div class="faq" style="left:612px;top:3696px">How do we know you're a real business?</div>
  <div class="faq" style="left:612px;top:3762px">How far in advance should i book my trip?</div>
  <div class="faq" style="left:612px;top:3828px">Do i need a passport?</div>
  <div class="faq" style="left:612px;top:3894px">What about the zika virus?</div>
  <div class="faq" style="left:612px;top:3960px">How do you compare with DealDrop, staybooker.example,<br>TripVista and similar discount sites?</div>
</section>

<footer>
  <div class="abs" style="left:87px;top:4242px;width:1026px;height:1px;background:var(--teal)"></div>
  <div class="brand" style="left:77px;top:4310px;width:130px"><div class="brand-mark" style="width:44px;height:44px"></div><div class="brand-name" style="font-size:14px">TRAVEL by MEREL</div></div>
  <h4 class="foot-h" style="left:379px;font-weight:400">Main Menu</h4>
  <ul class="foot-list" style="left:380px"><li>Home</li><li>About Me</li></ul>
  <h4 class="foot-h" style="left:654px;font-weight:400">Quick Links</h4>
  <ul class="foot-list" style="left:654px"><li>Contact Us</li><li>FAQ</li></ul>
  <h4 class="foot-h" style="left:1023px;font-weight:400">Get in touch</h4>
  <div class="abs" style="left:940px;top:4364px;width:110px;height:26px;border:1px solid #e3e3e3;font-size:9px;color:#999;padding:7px 6px">Enter your email here</div>
  <div class="abs" style="left:1051px;top:4364px;width:62px;height:26px;background:var(--teal);color:#fff;font-size:9px;display:flex;align-items:center;justify-content:center">Subscribe</div>
  <div class="bottom-bar">COPYRIGHT © 2024 · TRAVEL BY MEREL LLC • ALL RATES QUOTED ON THIS WEBSITE ARE SUBJECT TO CHANGE WITHOUT NOTICE</div>
</footer>

</body>
</html>
```